U.S. based testing, inspection, and certification (TIC) company needs a new social media design.

We need a social media design primarily for LinkedIn 1200x1200px for our U.S. based company with international capabilities for performing dozens if not hundreds of testing, inspection, and certification (TIC) services. Our primary services include calibration, chemical analysis, consulting engineering, environmental simulation, forensic engineering, materials testing, mechanical testing, and nondestructive testing. Industries we serve are aerospace/aviation, automotive, chemical, commercial properties, construction, consumer products, defense, energy storage, healthcare, insurance/legal, life science, manufacturing, oil & gas, power generation, pulp & paper, and telecommunications. https://veltrolabs.example/

Guideline hex colors (primary, secondary): #29aae2, #0b1f3b

The final design should communicate:
1. Trust, Integrity, and Independence
2. Technical Expertise and Accuracy
3. Efficiency and Speed
4. Value-Added Partnership

We previously used a hexagon design that we would like to part ways from; hexagon examples and KRV logos uploaded.

```html
<!DOCTYPE html>
<html lang="en">
<head>
<meta charset="utf-8">
<title>KRV – Precision You Can Count On</title>
<link rel="stylesheet" href="https://fonts.googleapis.com/css2?family=Montserrat:wght@600;700;800&family=Open+Sans:wght@400;600;700&display=swap">
<style>
  :root {
    --navy: #0b1f3b;
    --navy-panel: #12395e;
    --navy-card: #13233f;
    --card-line: #2a3a52;
    --blue: #29aae2;
    --white: #ffffff;
    --muted: #5f7189;
    --label: #8796aa;
  }
  * { margin: 0; padding: 0; box-sizing: border-box; }
  html, body { width: 1200px; height: 1200px; overflow: hidden; background: var(--navy); }
  .post {
    position: relative; width: 1200px; height: 1200px; overflow: hidden;
    background: var(--navy); color: var(--white);
    font-family: "Open Sans", Arial, sans-serif;
  }
  .top-bar { position: absolute; left: 0; top: 0; width: 1200px; height: 8px; background: var(--blue); }

  .brand { position: absolute; left: 80px; top: 62px; }
  .brand-mark {
    display: block; font-family: "Montserrat", sans-serif; font-weight: 800;
    font-size: 72px; line-height: 64px; letter-spacing: 8px; color: var(--white);
  }
  .brand-name { display: block; margin-top: 6px; font-size: 16px; color: var(--white); }

  .tagline-box {
    position: absolute; left: 80px; top: 186px; width: 1040px; height: 40px;
    border: 2px solid var(--blue); background: var(--navy-panel);
    font-size: 19px; letter-spacing: 1px; color: var(--blue);
    padding-left: 8px; line-height: 36px;
  }

  .headline {
    position: absolute; left: 86px; top: 268px;
    font-family: "Montserrat", sans-serif; font-weight: 800;
    font-size: 94px; line-height: 85px; letter-spacing: 1px;
  }
  .headline .accent { color: var(--blue); display: block; }
  .headline span { display: block; }
  .services-line {
    position: absolute; left: 92px; top: 538px;
    font-size: 29px; letter-spacing: 2.5px; color: var(--muted);
  }

  .hero-photo { position: absolute; left: 722px; top: 267px; width: 398px; height: 311px; }

  .divider { position: absolute; left: 80px; top: 609px; width: 1040px; height: 2px; background: var(--blue); }

  .stats { position: absolute; left: 80px; top: 630px; width: 1040px; display: flex; }
  .stat { width: 260px; padding-left: 0; position: relative; }
  .stat + .stat { padding-left: 26px; }
  .stat + .stat::before {
    content: ""; position: absolute; left: 0; top: 10px; width: 2px; height: 106px; background: var(--card-line);
  }
  .stat-value {
    font-family: "Montserrat", sans-serif; font-weight: 800; font-size: 66px;
    line-height: 72px; color: var(--blue);
  }
  .stat-label { margin-top: 8px; font-size: 15px; line-height: 20px; color: var(--label); }

  .service-grid {
    position: absolute; left: 80px; top: 787px; width: 1040px; height: 174px;
    display: grid; grid-template-columns: 1fr 1fr; grid-template-rows: repeat(3, 1fr);
    border: 1px solid var(--blue); background: var(--navy-panel);
  }
  .service-cell {
    border: 1px solid var(--blue); display: flex; align-items: center; justify-content: center;
    font-size: 20px; letter-spacing: 2px; color: var(--white);
  }

  .values {
    position: absolute; left: 80px; top: 1007px; width: 1040px; height: 59px;
    display: flex; border: 2px solid var(--card-line); background: var(--navy-card);
  }
  .value { flex: 1; display: flex; align-items: center; padding-left: 16px; gap: 10px; }
  .value + .value { border-left: 2px solid var(--card-line); }
  .value svg { width: 34px; height: 34px; flex: none; }
  .value-title { font-size: 11px; font-weight: 700; line-height: 13px; color: var(--white); }
  .value-sub { font-size: 9px; line-height: 12px; color: var(--label); }

  .footer-line { position: absolute; left: 0; top: 1136px; width: 1200px; height: 1px; background: var(--card-line); }
  .footer-url { position: absolute; left: 80px; top: 1160px; font-size: 12px; letter-spacing: 1.5px; color: var(--label); }
  .footer-claim {
    position: absolute; right: 66px; top: 1160px; font-family: "Montserrat", sans-serif;
    font-weight: 700; font-size: 13px; color: var(--blue);
  }
</style>
</head>
<body>
<main class="post">
  <div class="top-bar"></div>

  <div class="brand">
    <span class="brand-mark">KRV</span>
    <span class="brand-name">Kestrel Research Ventures</span>
  </div>

  <div class="tagline-box">TIC Services · U.S. Based · Global Reach</div>

  <h1 class="headline">
    <span>PRECISION</span>
    <span class="accent">YOU CAN</span>
    <span>COUNT ON.</span>
  </h1>
  <p class="services-line">TESTING · INSPECTION · CERTIFICATION</p>

  <svg class="hero-photo" viewBox="0 0 398 311" role="img" aria-label="Photo of a gloved hand placing a polished calibration weight on a laboratory balance">
    <defs>
      <linearGradient id="labPhoto" x1="0" y1="0" x2="1" y2="1">
        <stop offset="0" stop-color="#dfe9f2"/>
        <stop offset="0.5" stop-color="#a9bccd"/>
        <stop offset="1" stop-color="#5d6c7c"/>
      </linearGradient>
    </defs>
    <rect width="398" height="311" fill="url(#labPhoto)"/>
    <polygon points="0,0 78,0 22,311 0,311" fill="#29aae2"/>
  </svg>

  <div class="divider"></div>

  <section class="stats">
    <div class="stat"><div class="stat-value">100+</div><div class="stat-label">Distinct TIC<br>Services</div></div>
    <div class="stat"><div class="stat-value">16+</div><div class="stat-label">Industries<br>Served</div></div>
    <div class="stat"><div class="stat-value">50+</div><div class="stat-label">Years of<br>Experience</div></div>
    <div class="stat"><div class="stat-value">NQAB</div><div class="stat-label">Accredited<br>Laboratory</div></div>
  </section>

  <section class="service-grid">
    <div class="service-cell">TESTING</div>
    <div class="service-cell">FORENSICS</div>
    <div class="service-cell">INSPECTION</div>
    <div class="service-cell">ENGINEERING</div>
    <div class="service-cell">CALIBRATION</div>
    <div class="service-cell">TRAINING</div>
  </section>

  <section class="values">
    <div class="value">
      <svg viewBox="0 0 34 34"><circle cx="17" cy="17" r="15" fill="none" stroke="#29aae2" stroke-width="1.5"/><path d="M11 17.5l4 4 8-9" fill="none" stroke="#29aae2" stroke-width="1.5"/></svg>
      <div><div class="value-title">Independent</div><div class="value-sub">Unbiased Result</div></div>
    </div>
    <div class="value">
      <svg viewBox="0 0 34 34"><rect x="2" y="2" width="30" height="30" fill="none" stroke="#29aae2" stroke-width="1.5"/><path d="M17 4v26M4 17h26" stroke="#29aae2" stroke-width="1.5"/></svg>
      <div><div class="value-title">Accurate</div><div class="value-sub">Certified Data</div></div>
    </div>
    <div class="value">
      <svg viewBox="0 0 34 34"><circle cx="17" cy="17" r="15" fill="none" stroke="#29aae2" stroke-width="1.5"/><path d="M17 8v10l5 4" fill="none" stroke="#29aae2" stroke-width="1.5"/></svg>
      <div><div class="value-title">Efficient</div><div class="value-sub">Fast Turnaround</div></div>
    </div>
    <div class="value">
      <svg viewBox="0 0 34 34"><circle cx="17" cy="17" r="15" fill="none" stroke="#29aae2" stroke-width="1.5"/><path d="M10 21l5-5 3 3 6-6" fill="none" stroke="#29aae2" stroke-width="1.5"/></svg>
      <div><div class="value-title">Trusted Partner</div><div class="value-sub">End-to-End Value</div></div>
    </div>
  </section>

  <div class="footer-line"></div>
  <div class="footer-url">www.veltrolabs.example</div>
  <div class="footer-claim">FROM CONFIDENCE TO CERTAINTY</div>
</main>
</body>
</html>
```